Brightbay Business Card Design

Our company is called Brightbay. We manufacture confectionary snacks & frozen novelties. Our initial product portfolio includes frozen ice lollies/popsicles & stick ice cream bars.

We require a business card design.

Please use the attached Logo.

Please use an orange, brown, yellow colour code. You may choose any combination of the 3 or include all three. The logo however must remain orange.

Target Market(s)

Business card will be targeted at distributors of our products such as supermarket procurement managers, convenience store owners, wholesale distributors and merchandising agents.

Industry/Entity Type

Business

Requirements
Must have
• Calvin Obeng_Director/ P.O.Box Dunmore 5172, Accra, Ghana / m: 00233(0)507318924/ e: calvin.obeng@mailvora.co.uk

```html
<!DOCTYPE html>
<html lang="en">
<head>
<meta charset="utf-8">
<title>Brightbay Business Card</title>
<link rel="stylesheet" href="https://fonts.googleapis.com/css2?family=Montserrat:wght@400;700&display=swap">
<style>
  :root {
    --backdrop: #2b2b2b;
    --paper: #f1f1f0;
    --cocoa: #5e3628;
    --orange: #e0702f;
    --ink: #4e4e4e;
  }
  * { box-sizing: border-box; margin: 0; padding: 0; }
  html, body { width: 1200px; height: 896px; overflow: hidden; }
  body {
    background: var(--backdrop);
    position: relative;
    font-family: "Montserrat", Arial, sans-serif;
  }
  .card {
    position: absolute;
    top: 180px;
    height: 535px;
    border-radius: 22px;
  }
  .card::before {
    content: "";
    position: absolute;
    inset: 11px;
    border: 2px solid var(--orange);
    border-radius: 20px;
  }
  .card-front { left: 281px; width: 287px; background: var(--paper); }
  .card-back { left: 628px; width: 298px; background: var(--cocoa); }

  .brand {
    position: absolute;
    left: 0; right: 0;
    display: flex;
    align-items: center;
    justify-content: center;
    gap: 8px;
    color: var(--orange);
    font-weight: 700;
  }
  .brand-dot { border-radius: 50%; background: var(--orange); flex: none; }
  .card-front .brand { top: 268px; top: 88px; font-size: 30px; }
  .card-front .brand-dot { width: 18px; height: 18px; }
  .card-back .brand { top: 248px; font-size: 40px; }
  .card-back .brand-dot { width: 24px; height: 24px; }

  .holder {
    position: absolute;
    top: 268px; left: 0; right: 0;
    text-align: center;
    color: var(--ink);
  }
  .holder-name { font-size: 24px; font-weight: 400; letter-spacing: 0.5px; line-height: 28px; }
  .holder-role { font-size: 14px; line-height: 18px; }
  .rule {
    position: absolute;
    top: 327px; left: 25px; right: 14px;
    height: 5px;
    border-top: 1.5px solid var(--orange);
    border-bottom: 1.5px solid var(--orange);
  }
  .contact {
    position: absolute;
    top: 376px; left: 0; right: 0;
    text-align: center;
    color: var(--ink);
    font-size: 13.5px;
    list-style: none;
  }
  .contact li { line-height: 29px; }
  .contact .label { color: var(--orange); margin-right: 3px; }
  .contact .address { line-height: 16px; margin-top: 5px; }
</style>
</head>
<body>
  <section class="card card-front">
    <div class="brand"><span class="brand-dot"></span>Brightbay</div>
    <div class="holder">
      <p class="holder-name">Calvin Obeng</p>
      <p class="holder-role">Director</p>
    </div>
    <div class="rule"></div>
    <ul class="contact">
      <li><span class="label">M</span>00233(0)507318924</li>
      <li><span class="label">E</span>calvin.obeng@mailvora.co.uk</li>
      <li class="address">P.O.Box Dunmore 5172,<br>Accra, Ghana</li>
    </ul>
  </section>
  <section class="card card-back">
    <div class="brand"><span class="brand-dot"></span>Brightbay</div>
  </section>
</body>
</html>
```